Crunchy Spicy Sauce Label

We are looking for a label that would help our product stand out on a shelf. It has 3 flavor MILD, MEDIUM and SPICY with same ingredients. The company name is KANESA FOODS. KANESA means color green also it's funder's name. We would like the color green, brown or something natural colors in the label. These are oil based spicy sauce made of lots of crunchy and tasty ingredients such as fried onion, fried garlic, dried squid, sesame seed and almond. It is spicy but not too spicy, please don't use fire stuff in the label. The company information has to be small under the Nutrition Panel. The label size is 7"x2", filling 7cm diameter and 8cm tall glass jars.

Font styles to use
Sans Serif

Requirements
Must have
• Product Logo
Flavor
Net WT 225g
Nutrition Panel
Ingredients
Barcode
Company Information
Should not have
• Fire Design

```html
<!DOCTYPE html>
<html lang="en">
<head>
<meta charset="utf-8">
<title>Kobi Spicy Chili Sauce – Labels</title>
<link rel="stylesheet" href="https://fonts.googleapis.com/css2?family=Montserrat:wght@600;700;800&family=Arimo:wght@400;700&display=swap">
<style>
  :root {
    --page: #ffffff;
    --ink: #111111;
    --red: #c9302c;
    --cream: #fdfbea;
    --night: #181716;
    --bowl-green: #a3b43f;
    --bowl-dark: #4a4a2a;
    --rice: #e9e3d6;
  }
  * { box-sizing: border-box; margin: 0; padding: 0; }
  html, body { width: 1200px; height: 1000px; overflow: hidden; background: var(--page); }
  body { position: relative; font-family: "Arimo", Arial, sans-serif; color: var(--ink); }

  .label {
    position: absolute; left: 103px; width: 994px; height: 283px;
    --text: var(--ink);
    color: var(--text);
  }
  .label--mild   { top: 35px;  background: var(--page); }
  .label--medium { top: 358px; background: var(--cream); }
  .label--spicy  { top: 681px; background: var(--night); --text: #ffffff; }

  /* Nutrition panel */
  .nutrition { position: absolute; left: 35px; top: 32px; width: 260px; }
  .nutrition__title {
    font-family: "Montserrat", sans-serif; font-weight: 700; font-size: 15px;
    text-align: center; margin-left: 10px; line-height: 18px;
  }
  .nutrition__serving {
    display: flex; justify-content: space-between; margin-top: 10px; padding: 0 15px 0 10px;
    font-family: "Montserrat", sans-serif; font-weight: 700; font-size: 11px; line-height: 14px;
  }
  .nutrition__table { margin-top: 9px; border-top: 4px solid var(--text); border-bottom: 4px solid var(--text); }
  .nutrition__row {
    display: flex; justify-content: space-between; padding: 0 15px 0 10px;
    font-size: 11px; line-height: 14.5px; border-top: 1px solid var(--text);
  }
  .nutrition__row:first-child { border-top: 0; margin-top: 2px; }
  .nutrition__note { font-size: 11px; margin-top: 6px; padding-left: 8px; }

  .company { position: absolute; left: 35px; top: 231px; width: 260px; text-align: center; font-size: 11px; line-height: 12px; }
  .company__name { font-family: "Montserrat", sans-serif; font-weight: 700; }

  /* Center brand block */
  .brand { position: absolute; left: 354px; top: 0; width: 280px; height: 283px; text-align: center; }
  .brand__name {
    position: absolute; top: 84px; left: 0; width: 100%; white-space: nowrap;
    font-family: "Montserrat", sans-serif; font-weight: 800; font-size: 20px; line-height: 24px; color: var(--text);
  }
  .brand__art { position: absolute; left: 71px; top: 120px; width: 187px; height: 123px; }
  .brand__flavor {
    position: absolute; left: 80px; top: 186px; width: 120px;
    font-family: "Montserrat", sans-serif; font-weight: 800; font-size: 17px; line-height: 20px; color: var(--ink);
  }
  .label--spicy .brand__flavor { color: #ffffff; }
  .brand__net {
    position: absolute; top: 256px; left: 0; width: 100%;
    font-family: "Montserrat", sans-serif; font-weight: 700; font-size: 11px; line-height: 14px;
  }

  /* Right info column */
  .info { position: absolute; left: 698px; top: 32px; width: 262px; text-align: center; }
  .info__tagline { font-family: "Montserrat", sans-serif; font-weight: 700; font-size: 14.5px; line-height: 18px; color: var(--red); }
  .info__heading { font-family: "Montserrat", sans-serif; font-weight: 700; font-size: 14px; margin-top: 13px; line-height: 15px; }
  .info__text { font-size: 15px; line-height: 15.8px; }
  .info__line { display: block; text-align: justify; text-align-last: justify; white-space: nowrap; }
  .info__line--end { text-align: center; text-align-last: center; }
</style>
</head>
<body>

<section class="label label--mild">
  <div class="nutrition">
    <h2 class="nutrition__title">Nutrition Facts:</h2>
    <div class="nutrition__serving"><span>Serving Size</span><span>5G</span></div>
    <div class="nutrition__table">
      <div class="nutrition__row"><span>Calories</span><span>0%</span></div>
      <div class="nutrition__row"><span>Total Fat</span><span>0%</span></div>
      <div class="nutrition__row"><span>Cholesterol</span><span>0%</span></div>
      <div class="nutrition__row"><span>Sodium</span><span>0%</span></div>
      <div class="nutrition__row"><span>Total Carbohydrate</span><span>0%</span></div>
      <div class="nutrition__row"><span>Protein</span><span>0%</span></div>
    </div>
    <p class="nutrition__note">•Based in a 2,000 calories diet</p>
  </div>
  <div class="company">
    <p class="company__name">KANESA FOODS</p>
    <p>info@kanesafoods.ca</p>
    <p>www.kanesafoods.ca</p>
  </div>
  <div class="brand">
    <h1 class="brand__name">Kobi Spicy Chili Sauce</h1>
    <svg class="brand__art" viewBox="0 0 187 123" role="img" aria-label="Illustration of a green rice bowl topped with chili sauce, with two red chili peppers">
      <defs>
        <linearGradient id="art-mild" x1="0" y1="0" x2="0" y2="1">
          <stop offset="0" stop-color="#e9e3d6"/><stop offset="0.45" stop-color="#a3b43f"/><stop offset="1" stop-color="#4a4a2a"/>
        </linearGradient>
      </defs>
      <rect x="0" y="0" width="187" height="123" rx="18" fill="url(#art-mild)"/>
    </svg>
    <p class="brand__flavor">MILD</p>
    <p class="brand__net">NET. WT. 225G</p>
  </div>
  <div class="info">
    <p class="info__tagline">The Flavor That Brings You Home.</p>
    <h3 class="info__heading">Try it on...</h3>
    <p class="info__text">
      <span class="info__line">Fried Rice, Chaw-men, Ramen,</span>
      <span class="info__line">Dumpling, Pasta or anything you like!</span>
    </p>
    <h3 class="info__heading">Ingredients:</h3>
    <p class="info__text">
      <span class="info__line">Canola Oil, Sesame Oil, Onion,</span>
      <span class="info__line">Garlic, Almond, Sesame Seeds, Chili</span>
      <span class="info__line">Pepper, Soy Sauce, Salt, Sugar,</span>
      <span class="info__line">Seaweed, Monosodium Glutamate,</span>
      <span class="info__line info__line--end">Oyster Extractives</span>
    </p>
  </div>
</section>

<section class="label label--medium">
  <div class="nutrition">
    <h2 class="nutrition__title">Nutrition Facts:</h2>
    <div class="nutrition__serving"><span>Serving Size</span><span>5G</span></div>
    <div class="nutrition__table">
      <div class="nutrition__row"><span>Calories</span><span>0%</span></div>
      <div class="nutrition__row"><span>Total Fat</span><span>0%</span></div>
      <div class="nutrition__row"><span>Cholesterol</span><span>0%</span></div>
      <div class="nutrition__row"><span>Sodium</span><span>0%</span></div>
      <div class="nutrition__row"><span>Total Carbohydrate</span><span>0%</span></div>
      <div class="nutrition__row"><span>Protein</span><span>0%</span></div>
    </div>
    <p class="nutrition__note">•Based in a 2,000 calories diet</p>
  </div>
  <div class="company">
    <p class="company__name">KANESA FOODS</p>
    <p>info@kanesafoods.ca</p>
    <p>www.kanesafoods.ca</p>
  </div>
  <div class="brand">
    <h1 class="brand__name">Kobi Spicy Chili Sauce</h1>
    <svg class="brand__art" viewBox="0 0 187 123" role="img" aria-label="Illustration of a green rice bowl topped with chili sauce, with two red chili peppers">
      <defs>
        <linearGradient id="art-medium" x1="0" y1="0" x2="0" y2="1">
          <stop offset="0" stop-color="#e9e3d6"/><stop offset="0.45" stop-color="#a3b43f"/><stop offset="1" stop-color="#4a4a2a"/>
        </linearGradient>
      </defs>
      <rect x="0" y="0" width="187" height="123" rx="18" fill="url(#art-medium)"/>
    </svg>
    <p class="brand__flavor">MEDIUM</p>
    <p class="brand__net">NET. WT. 225G</p>
  </div>
  <div class="info">
    <p class="info__tagline">The Flavor That Brings You Home.</p>
    <h3 class="info__heading">Try it on...</h3>
    <p class="info__text">
      <span class="info__line">Fried Rice, Chaw-men, Ramen,</span>
      <span class="info__line">Dumpling, Pasta or anything you like!</span>
    </p>
    <h3 class="info__heading">Ingredients:</h3>
    <p class="info__text">
      <span class="info__line">Canola Oil, Sesame Oil, Onion,</span>
      <span class="info__line">Garlic, Almond, Sesame Seeds, Chili</span>
      <span class="info__line">Pepper, Soy Sauce, Salt, Sugar,</span>
      <span class="info__line">Seaweed, Monosodium Glutamate,</span>
      <span class="info__line info__line--end">Oyster Extractives</span>
    </p>
  </div>
</section>

<section class="label label--spicy">
  <div class="nutrition">
    <h2 class="nutrition__title">Nutrition Facts:</h2>
    <div class="nutrition__serving"><span>Serving Size</span><span>5G</span></div>
    <div class="nutrition__table">
      <div class="nutrition__row"><span>Calories</span><span>0%</span></div>
      <div class="nutrition__row"><span>Total Fat</span><span>0%</span></div>
      <div class="nutrition__row"><span>Cholesterol</span><span>0%</span></div>
      <div class="nutrition__row"><span>Sodium</span><span>0%</span></div>
      <div class="nutrition__row"><span>Total Carbohydrate</span><span>0%</span></div>
      <div class="nutrition__row"><span>Protein</span><span>0%</span></div>
    </div>
    <p class="nutrition__note">•Based in a 2,000 calories diet</p>
  </div>
  <div class="company">
    <p class="company__name">KANESA FOODS</p>
    <p>info@kanesafoods.ca</p>
    <p>www.kanesafoods.ca</p>
  </div>
  <div class="brand">
    <h1 class="brand__name">Kobi Spicy Chili Sauce</h1>
    <svg class="brand__art" viewBox="0 0 187 123" role="img" aria-label="Illustration of a green rice bowl topped with chili sauce, with two red chili peppers">
      <defs>
        <linearGradient id="art-spicy" x1="0" y1="0" x2="0" y2="1">
          <stop offset="0" stop-color="#e9e3d6"/><stop offset="0.45" stop-color="#a3b43f"/><stop offset="1" stop-color="#4a4a2a"/>
        </linearGradient>
      </defs>
      <rect x="0" y="0" width="187" height="123" rx="18" fill="url(#art-spicy)"/>
    </svg>
    <p class="brand__flavor">SPICY</p>
    <p class="brand__net">NET. WT. 225G</p>
  </div>
  <div class="info">
    <p class="info__tagline">The Flavor That Brings You Home.</p>
    <h3 class="info__heading">Try it on...</h3>
    <p class="info__text">
      <span class="info__line">Fried Rice, Chaw-men, Ramen,</span>
      <span class="info__line">Dumpling, Pasta or anything you like!</span>
    </p>
    <h3 class="info__heading">Ingredients:</h3>
    <p class="info__text">
      <span class="info__line">Canola Oil, Sesame Oil, Onion,</span>
      <span class="info__line">Garlic, Almond, Sesame Seeds, Chili</span>
      <span class="info__line">Pepper, Soy Sauce, Salt, Sugar,</span>
      <span class="info__line">Seaweed, Monosodium Glutamate,</span>
      <span class="info__line info__line--end">Oyster Extractives</span>
    </p>
  </div>
</section>

</body>
</html>
```